Startup photography business has a new logo, now we need business cards

Design a business card for the two partners of our business.
Our business Brisk Pelican has a new logo and we need to design a business card to showcase it and us.
Our colours of blue and orange are punchy and vivid, but how can we make the most of it on our card?

It should have our name Brisk Pelican
name of partner
phone number
email
website

Industry/Entity Type

Professional Photography

Contact Information for Business Card

Tom Ashworth
+61 400 55 61 72
tom@briskpelican.com.au
briskpelican.com.au

second card
Neil Porter
+61 400 918 263
tom@briskpelican.com.au
briskpelican.com.au

Colors
f37122
f68d4c
33a6d7
0592cd

Requirements
Must have
• one version of our logo, we have included options
• Name
• phone number
• email
• website
Nice to have
• instagram briskpelicanmedia
• twitter briskpelicanmedia
• facebook briskpelicanmedia

```html
<!DOCTYPE html>
<html lang="en">
<head>
<meta charset="utf-8">
<title>Brisk Pelican – Business Cards</title>
<link href="https://fonts.googleapis.com/css2?family=Passion+One&family=Tinos&family=Arimo&display=swap" rel="stylesheet">
<style>
  :root {
    --page: #e9e6e1;
    --card-white: #ffffff;
    --band: #000000;
    --brand-blue: #33a6d7;
    --brand-blue-deep: #0592cd;
    --brand-orange: #f37122;
    --brand-orange-soft: #f68d4c;
    --back-blue: #33a6d7;
    --text-light: #ffffff;
  }
  * { box-sizing: border-box; margin: 0; padding: 0; }
  html, body { width: 1200px; height: 892px; overflow: hidden; }
  body {
    background: var(--page);
    position: relative;
    font-family: "Arimo", Arial, sans-serif;
  }
  .card {
    position: absolute;
    top: 281px;
    width: 540px;
    height: 330px;
    border-radius: 4px;
    box-shadow: 0 10px 28px rgba(0,0,0,.22);
    overflow: hidden;
  }
  .card--front { left: 40px; background: var(--card-white); }
  .card--back  { left: 620px; background: var(--back-blue); }

  .brand {
    position: absolute;
    display: flex;
    align-items: center;
    gap: 14px;
    font-family: "Passion One", Impact, sans-serif;
    font-weight: 400;
    text-transform: uppercase;
    letter-spacing: 1px;
    white-space: nowrap;
  }
  .brand__dot { border-radius: 50%; flex: none; background: var(--brand-orange); }

  .card--front .brand {
    left: 50%; top: 40px; transform: translateX(-50%);
    color: var(--brand-blue);
    font-size: 46px;
  }
  .card--front .brand__dot { width: 34px; height: 34px; }

  .card--back .brand {
    left: 50%; top: 50%; transform: translate(-50%, -50%);
    color: var(--text-light);
    font-size: 62px;
  }
  .card--back .brand__dot { width: 48px; height: 48px; }

  .contact-band {
    position: absolute;
    left: 0; right: 0;
    top: 142px; height: 142px;
    background: var(--band);
    display: flex;
    align-items: center;
    padding: 0 16px;
  }
  .person-name {
    font-family: "Tinos", "Times New Roman", serif;
    color: var(--brand-blue);
    font-size: 24px;
    white-space: nowrap;
    line-height: 1.1;
    flex: none;
  }
  .divider {
    width: 1px; height: 78px;
    background: #ffffff;
    margin: 0 12px 0 14px;
    flex: none;
  }
  .contact-list { list-style: none; color: var(--text-light); font-size: 12.5px; }
  .contact-list li { display: flex; align-items: center; gap: 7px; line-height: 24px; white-space: nowrap; }
  .contact-list--social { flex: none; }
  .contact-list--direct { margin-left: 16px; flex: none; }
  .icon {
    width: 14px; height: 14px; flex: none;
    background: var(--brand-blue);
    border-radius: 2px;
    display: flex; align-items: center; justify-content: center;
  }
  .icon svg { width: 10px; height: 10px; }
</style>
</head>
<body>

  <section class="card card--front" aria-label="Business card front">
    <div class="brand">
      <span class="brand__dot"></span>
      <span class="brand__name">Brisk Pelican</span>
    </div>

    <div class="contact-band">
      <p class="person-name">Tom Ashworth</p>
      <span class="divider"></span>
      <ul class="contact-list contact-list--social">
        <li><span class="icon"></span>briskpelicanmedia</li>
        <li><span class="icon"></span>briskpelicanmedia</li>
        <li><span class="icon"></span>briskpelicanmedia</li>
      </ul>
      <ul class="contact-list contact-list--direct">
        <li>
          <span class="icon"><svg viewBox="0 0 12 12"><path d="M3 1l2 2.5-1.2 1.2a6 6 0 0 0 3.5 3.5L8.5 7 11 9l-1.5 2C5 11 1 7 1 2.5z" fill="#000"/></svg></span>
          +61 400 55 61 72
        </li>
        <li>
          <span class="icon"><svg viewBox="0 0 12 12"><circle cx="6" cy="6" r="4.5" fill="none" stroke="#000" stroke-width="1.2"/><path d="M1.5 6h9M6 1.5c-2 2.5-2 6.5 0 9M6 1.5c2 2.5 2 6.5 0 9" fill="none" stroke="#000" stroke-width="1"/></svg></span>
          www.briskpelican.com.au
        </li>
        <li>
          <span class="icon"><svg viewBox="0 0 12 12"><rect x="1" y="2.5" width="10" height="7" fill="none" stroke="#000" stroke-width="1.2"/><path d="M1 2.5l5 4 5-4" fill="none" stroke="#000" stroke-width="1.2"/></svg></span>
          tom@briskpelican.com.au
        </li>
      </ul>
    </div>
  </section>

  <section class="card card--back" aria-label="Business card back">
    <div class="brand">
      <span class="brand__dot"></span>
      <span class="brand__name">Brisk Pelican</span>
    </div>
  </section>

</body>
</html>
```